Wavelark Yoga Singapore leaflet

I need a leaflet for Wavelark Yoga Singapore. The logo has been included as file 1 but I need the logo to be circular (It's a square now so I need it cropped into a circle which includes the circle of paddles).

There should be 2 sides to the leaflet. One side will feature a single landscape photograph of a group doing SUP Yoga (File 2). On that page, I would like the following quote to be included, 'Smell the sea and feel the sky, Let your soul and spirit fly, into the mystic...--Hal Brennick' If it's possible to include the logo (circular) and the company slogan 'Breathe Flow Core', please do.

On the other page, it has to include the photo of the instructor which may be cropped if deemed necessary (file 3). To accompany the photo of the instructor is the following short write-up of the instructor, 'Tamsin Okafor enjoys sharing her love for teaching and yoga not just on land but on the SUP board as well. She is a 200h RYT with Posture Registry who is BWG (Board of Wavecraft Guides) certified for Water Rescue, SUP level 1, SUP yoga and First Aid (and CPR) certified.' and a quote from the instructor, 'To find your breath as you move on the board at sea, void of the hustle and bustle of city life, is itself calming and meditative.' -- Tamsin Okafor

On the same page, the following information about classes and rates need to be included:

SUP Yoga
Single class: S$50 per person
3-class card (valid for 6 weeks): S$135 per person
5-class card (valid for 10 weeks): S$210 per person
Each class is for an hour at Kestrel Bay Green.
Corporate events or private sessions can be organised to include SUP Yoga and/or yoga/pilates.
SUP Yoga sessions may be organised at private swimming pools or at other marine locations around Singapore.
For further details or reservations, please email wavelarkyoga@postvane.com.

At the bottom of this page, please include the following (These may be included in the same line):
Wavelark Yoga Singapore (Reg. No. 71849025K)
wavelarkyoga@postvane.com
friendwall.com/WavelarkYoga

Any of the photos from files 4 to 6 may be included in the page with the majority of the information.

Hi everyone! Thank you for all your effort and designs! I've already picked the design that stood out the most. Thank you once again!

```html
<!DOCTYPE html>
<html lang="en">
<head>
<meta charset="utf-8">
<title>Wavelark Yoga Singapore — Leaflet</title>
<link rel="stylesheet" href="https://fonts.googleapis.com/css2?family=Bebas+Neue&family=Open+Sans:wght@400;600&display=swap">
<style>
  :root {
    --page-bg: #e6e8ec;
    --slate: #434a5e;
    --sky-blue: #5db4e8;
    --white: #ffffff;
    --photo-sky: #dfe3e7;
    --photo-sea: #8ea4b4;
  }
  * { box-sizing: border-box; margin: 0; padding: 0; }
  html, body {
    width: 1200px; height: 1000px; overflow: hidden;
    background: var(--page-bg);
  }
  .canvas {
    position: relative; width: 1200px; height: 1000px;
    display: flex; align-items: center; justify-content: center;
  }
  .leaflet {
    position: relative; width: 664px; height: 940px;
    background: var(--slate); overflow: hidden;
    box-shadow: 0 6px 24px rgba(0,0,0,.18);
  }
  .leaflet__hero {
    position: absolute; left: 0; top: 0;
    width: 664px; height: 940px;
  }
  .brand-badge {
    position: absolute; left: 318px; top: 448px;
    width: 230px; height: 230px; border-radius: 50%;
    background: var(--sky-blue);
    display: flex; align-items: center; justify-content: center;
    text-align: center;
  }
  .brand-badge__name {
    font-family: "Bebas Neue", sans-serif;
    font-size: 38px; line-height: 1; letter-spacing: 1px;
    color: var(--white); width: 170px;
  }
  .slogan {
    position: absolute; left: 318px; top: 696px; width: 230px;
    text-align: center;
    font-family: "Bebas Neue", sans-serif;
    font-size: 34px; letter-spacing: 1px;
    color: var(--sky-blue);
  }
  .quote {
    position: absolute; left: 28px; right: 28px; top: 818px;
    font-family: "Open Sans", sans-serif;
    font-size: 11.5px; color: var(--white); text-align: center;
  }
  .social-band {
    position: absolute; left: 0; right: 0; bottom: 0; height: 76px;
    background: var(--sky-blue);
    display: flex; align-items: center; justify-content: space-around;
    padding: 0 16px;
  }
  .social-band__item {
    display: flex; align-items: center; gap: 8px;
    font-family: "Bebas Neue", sans-serif;
    font-size: 21px; letter-spacing: .5px; color: var(--white);
  }
  .social-band__dot {
    width: 14px; height: 14px; border-radius: 50%;
    background: var(--white); flex: none;
  }
</style>
</head>
<body>
<main class="canvas">
  <article class="leaflet">
    <svg class="leaflet__hero" viewBox="0 0 664 940" aria-hidden="false">
      <defs>
        <linearGradient id="photo-tone" x1="0" y1="0" x2="0" y2="1">
          <stop offset="0" stop-color="var(--photo-sky)"/>
          <stop offset="0.52" stop-color="#c9d0d6"/>
          <stop offset="0.6" stop-color="var(--photo-sea)"/>
          <stop offset="1" stop-color="#7b93a3"/>
        </linearGradient>
      </defs>
      <path class="hero__arc-band" d="M0 0 H498 A498 600 0 0 1 0 600 Z" fill="var(--sky-blue)"/>
      <path class="hero__photo" role="img" aria-label="Photo of a group practising yoga on stand-up paddleboards at sea, windsurfers and ships on the horizon"
            d="M0 0 H476 A476 576 0 0 1 0 576 Z" fill="url(#photo-tone)"/>
    </svg>

    <div class="brand-badge">
      <span class="brand-badge__name">Wavelark Yoga Singapore</span>
    </div>

    <p class="slogan">Breathe Flow Core</p>

    <p class="quote">Smell the sea and feel the sky, Let your soul and spirit fly, into the mystic...--Hal Brennick</p>

    <footer class="social-band">
      <span class="social-band__item"><span class="social-band__dot"></span>Wavelark Yoga Singapore</span>
      <span class="social-band__item"><span class="social-band__dot"></span>Wavelark Yoga Singapore</span>
      <span class="social-band__item"><span class="social-band__dot"></span>Wavelark Yoga Singapore</span>
    </footer>
  </article>
</main>
</body>
</html>
```